Mental health agency needs an ad for brochure

Please provide us with a half page (W 8.5 inches x H 5.5 inches) advertising our company. We are a mental health agency that provides training, education, and consultation for companies that serve children, adolescents, or adults. We can offer training and education to help companies better serve their clientele and consultation about how companies are currently working with their staff or clientele. Our website is www.bridgelumen.com and they can contact us at info@kestrelhollowinstitute.com or 503-274-8816.

```html
<!DOCTYPE html>
<html lang="en">
<head>
<meta charset="utf-8">
<title>Kestrel Hollow Institute – Half Page Ad</title>
<link href="https://fonts.googleapis.com/css2?family=Noto+Serif:wght@400;700&display=swap" rel="stylesheet">
<style>
  :root {
    --navy: #0b2f73;
    --deep-blue: #053d7f;
    --mid-blue: #0a6aa8;
    --teal: #0f9cc2;
    --grey-text: #6b6b6b;
    --white: #ffffff;
    --page: #e6e6e6;
  }
  * { margin: 0; padding: 0; box-sizing: border-box; }
  html, body { width: 1200px; height: 1031px; overflow: hidden; background: var(--page); }
  body { font-family: "Noto Serif", Georgia, serif; position: relative; }

  .ad {
    position: absolute; left: 20px; top: 140px;
    width: 1160px; height: 751px;
    background: var(--white);
    overflow: hidden;
  }
  .ad-shapes { position: absolute; inset: 0; }

  .headline {
    position: absolute; left: 53px; top: 36px;
    border-left: 5px solid var(--navy);
    padding-left: 18px;
    font-size: 47px; line-height: 58px;
    color: var(--grey-text);
  }
  .headline .strong-navy { color: var(--navy); font-weight: 700; }
  .headline .strong-teal { color: var(--teal); font-weight: 700; }

  .intro-tag {
    position: absolute; left: 51px; top: 319px;
    width: 135px; height: 35px;
    background: var(--teal);
    clip-path: polygon(0 0, 88% 0, 100% 100%, 0 100%);
    color: var(--white); font-weight: 700; font-size: 24px;
    padding-left: 8px; line-height: 35px;
  }
  .intro-rule {
    position: absolute; left: 51px; width: 418px; height: 2px;
    background: var(--teal);
  }
  .intro-rule.top { top: 354px; }
  .intro-rule.mid { top: 573px; }

  .body-copy {
    position: absolute; left: 51px; width: 430px;
    color: var(--white); font-size: 18.3px; line-height: 24.6px;
  }
  .body-copy strong { font-weight: 700; }
  .body-copy.first { top: 361px; }
  .body-copy.second { top: 578px; }

  .photo {
    position: absolute; border-radius: 50%;
  }
  .photo.family {
    left: 619px; top: 84px; width: 484px; height: 484px;
    background: radial-gradient(circle at 40% 30%, #8fb86a, #5f8a45 45%, #c9b7a6 75%, #e9e4df);
  }
  .photo.couple {
    left: 577px; top: 433px; width: 220px; height: 220px;
    border: 8px solid #7fa0c4;
    background: radial-gradient(circle at 55% 55%, #f0e6de, #b9aaa0 55%, #3b3b3b);
  }

  .brand-badge {
    position: absolute; left: 892px; top: 447px;
    width: 192px; height: 192px; border-radius: 50%;
    background: var(--white);
    display: flex; flex-direction: column; align-items: center; justify-content: center;
    text-align: center; color: var(--navy);
    font-size: 15px; font-weight: 700; line-height: 20px;
  }

  .contact-bar {
    position: absolute; left: 0; right: 0; top: 692px; height: 59px;
    display: flex; align-items: center; padding-left: 51px;
    font-size: 25px; color: var(--navy);
  }
  .contact-item { display: flex; align-items: center; gap: 9px; }
  .contact-item strong { font-weight: 700; }
  .contact-item .hl { color: var(--teal); font-weight: 700; }
  .divider { width: 2px; height: 22px; background: var(--teal); margin: 0 22px; }
  .icon { width: 24px; height: 24px; flex: none; }
</style>
</head>
<body>
  <div class="ad">
    <svg class="ad-shapes" width="1160" height="751" viewBox="0 0 1160 751">
      <defs>
        <linearGradient id="panelBlue" x1="0" y1="0" x2="1" y2="0">
          <stop offset="0" stop-color="#0a5f9e"/>
          <stop offset="0.55" stop-color="#053c7d"/>
          <stop offset="1" stop-color="#0a74ac"/>
        </linearGradient>
      </defs>
      <!-- teal wave -->
      <path d="M0 283 C120 200 270 190 400 240 C520 285 640 340 760 380 L1160 380 L1160 692 L0 692 Z" fill="var(--teal)"/>
      <!-- navy wave -->
      <path d="M0 330 C130 250 280 240 420 280 C540 315 650 360 770 400 L1160 400 L1160 692 L0 692 Z" fill="var(--navy)"/>
      <!-- main blue panel -->
      <path d="M0 360 C150 300 300 300 440 340 C560 375 690 430 820 450 C950 460 1080 420 1160 350 L1160 692 L0 692 Z" fill="url(#panelBlue)"/>
      <!-- dark ring around family photo -->
      <path d="M1085 190 A300 285 0 1 0 1000 600" fill="none" stroke="var(--navy)" stroke-width="34"/>
      <!-- ring around badge -->
      <circle cx="988" cy="543" r="106" fill="none" stroke="var(--navy)" stroke-width="14"/>
    </svg>

    <h1 class="headline">
      <span class="strong-navy">Nurture Authentic</span><br>
      and <span class="strong-teal">Safe Relationships</span><br>
      Around You
    </h1>

    <div class="photo family" role="img" aria-label="Photo of a smiling family of four outdoors giving thumbs up"></div>
    <div class="photo couple" role="img" aria-label="Photo of a laughing couple embracing at home"></div>

    <div class="brand-badge">Kestrel Hollow<br>Institute, LLC</div>

    <div class="intro-tag">We are a</div>
    <div class="intro-rule top"></div>
    <p class="body-copy first"><strong>Mental health agency</strong> that provides training, education, and consultation in many different areas of expertise to help companies more effectively serve their clientele. We can consult about your company is currently working with your staff and clientele or focus on future company goals to provide a safer and more nurturing environment.</p>
    <div class="intro-rule mid"></div>
    <p class="body-copy second"><strong>We have a heat mapping tool</strong> targeting seven areas affecting staff morale, job satisfaction, and production that can quickly find problems among teams and departments.</p>

    <div class="contact-bar">
      <div class="contact-item">
        <svg class="icon" viewBox="0 0 24 24"><circle cx="12" cy="12" r="12" fill="var(--teal)"/><path d="M8 6l2 3-1.3 1.3a8 8 0 0 0 5 5L15 14l3 2-1 2.3C11 18 6 13 5.7 7z" fill="#fff"/></svg>
        <strong>503-274-8816</strong>
      </div>
      <span class="divider"></span>
      <div class="contact-item">
        <svg class="icon" viewBox="0 0 24 24"><circle cx="12" cy="12" r="12" fill="var(--teal)"/><rect x="6" y="8" width="12" height="8" rx="1" fill="#fff"/><path d="M6.5 8.5l5.5 4 5.5-4" fill="none" stroke="var(--teal)" stroke-width="1.2"/></svg>
        <span>info@<span class="hl">kestrelhollowinstitute</span>.com</span>
      </div>
      <span class="divider"></span>
      <div class="contact-item">
        <svg class="icon" viewBox="0 0 24 24"><circle cx="12" cy="12" r="12" fill="var(--teal)"/><g fill="none" stroke="#fff" stroke-width="1.2"><circle cx="12" cy="12" r="6"/><ellipse cx="12" cy="12" rx="2.6" ry="6"/><path d="M6 12h12M7 9h10M7 15h10"/></g></svg>
        <span>www.<span class="hl">bridgelumen</span>.com</span>
      </div>
    </div>
  </div>
</body>
</html>
```